New BROVANEL keyboard

We need to redesign the plastic cover of electronic keyboard. The equipment is a cooker with an agitation system. See page http://www.valtor-kitchenworks.com/catering-machinery/industrial-kitchens-equipment/tilting-bratt-pan where you can even find a video.

One of the important features of this equipment is the mixing system. We need to give more importance on the keypad and renew all buttons and general design.

Note: On the manual instruction you can find the keypad description. The keys 13, 14 and 15 can be moved. The rest (1-12) must remain on same postion.

Reason: Uploaded dimensions (mm 95x150) and logo

```html
<!DOCTYPE html>
<html lang="en">
<head>
<meta charset="utf-8">
<title>BROVANEL keypad cover</title>
<link rel="stylesheet" href="https://fonts.googleapis.com/css2?family=Open+Sans:wght@700&display=swap">
<style>
  :root {
    --page: #ffffff;
    --edge: #8a8a8a;
    --panel: #1c1c1c;
    --white: #ffffff;
    --red: #ef3338;
    --red-deep: #e21f26;
    --grey-key: #999999;
    --grey-clock: #8c8c8c;
    --lime: #8dc63f;
    --display: #cfcfcf;
    --steel: #66939a;
    --orange: #ff6a00;
    --teal: #33cc99;
    --green: #009933;
    --pale: #cccccc;
    --lavender: #9999ff;
    --knob: #8e8e8e;
    --knob-ring: #4a4a4a;
    --estop-ring: #fbd27a;
    --estop-button: #ee2222;
    --ink: #111111;
  }
  html, body { margin: 0; padding: 0; overflow: hidden; }
  body { width: 1200px; height: 2449px; background: var(--page); font-family: 'Open Sans', Arial, sans-serif; }
  .cover {
    position: relative; width: 586px; height: 1198px;
    border: 1px solid var(--edge); background: var(--page);
    transform: scale(2.0408, 2.0408); transform-origin: 0 0;
  }
  .keypad {
    position: absolute; left: 64px; top: 47px; width: 469px; height: 733px;
    background: var(--panel); border-radius: 10px;
  }
  .key { position: absolute; width: 99px; height: 103px; }
  .key svg { width: 100%; height: 100%; display: block; }
  .display { position: absolute; left: 22px; width: 206px; height: 102px; background: var(--display); border-radius: 7px; }
  .key-label { font-family: 'Open Sans', Arial, sans-serif; font-weight: 700; fill: var(--white); }
  .knob { position: absolute; left: 290px; top: 487px; width: 110px; height: 110px; }
  .estop { position: absolute; left: 160px; top: 833px; width: 280px; height: 280px; }
</style>
</head>
<body>
<div class="cover">
  <div class="keypad">
    <!-- row 1 -->
    <div class="key power" style="left:21px;top:21px;background:var(--red)">
      <svg viewBox="0 0 99 103"><rect x="17" y="18" width="65" height="67" rx="13" fill="none" stroke="#fff" stroke-width="7"/><line x1="49.5" y1="33" x2="49.5" y2="70" stroke="#fff" stroke-width="7"/></svg>
    </div>
    <div class="key probe-temp" style="left:242px;top:21px;background:var(--grey-key)">
      <svg viewBox="0 0 99 103"><path d="M33 14 a8 8 0 0 1 16 0 v45 a16 16 0 1 1 -16 0z" fill="#fff"/><path d="M37 14 a4 4 0 0 1 8 0 v48 a12 12 0 1 1 -8 0z" fill="var(--orange)"/><circle cx="41" cy="74" r="7" fill="#fff"/><line x1="76" y1="22" x2="76" y2="90" stroke="#fff" stroke-width="4"/><circle cx="76" cy="19" r="6" fill="#fff"/></svg>
    </div>
    <div class="key start-stop" style="left:350px;top:21px;background:var(--lime)">
      <svg viewBox="0 0 99 103"><rect x="17" y="18" width="65" height="67" rx="13" fill="none" stroke="#fff" stroke-width="6"/><text class="key-label" x="49.5" y="47" font-size="13" text-anchor="middle">START</text><text class="key-label" x="49.5" y="67" font-size="13" text-anchor="middle" letter-spacing="1">STOP</text></svg>
    </div>
    <!-- displays & arrows -->
    <div class="display" style="top:143px"></div>
    <div class="display" style="top:252px"></div>
    <div class="key up" style="left:242px;top:143px;background:var(--steel)">
      <svg viewBox="0 0 99 103"><path d="M49.5 14 L77 78 Q60 70 52 72 V86 H47 V72 Q39 70 22 78 Z" fill="#fff"/></svg>
    </div>
    <div class="key set-temp" style="left:350px;top:143px;background:var(--orange)">
      <svg viewBox="0 0 99 103"><path d="M41 22 a8.5 8.5 0 0 1 17 0 v37 a17 17 0 1 1 -17 0z" fill="none" stroke="#fff" stroke-width="5"/><circle cx="49.5" cy="73" r="7" fill="#fff"/><line x1="49.5" y1="42" x2="49.5" y2="70" stroke="#fff" stroke-width="4"/></svg>
    </div>
    <div class="key down" style="left:242px;top:252px;background:var(--steel)">
      <svg viewBox="0 0 99 103"><path d="M49.5 86 L77 24 Q60 32 52 30 V16 H47 V30 Q39 32 22 24 Z" fill="#fff"/></svg>
    </div>
    <div class="key timer" style="left:350px;top:252px;background:var(--grey-clock)">
      <svg viewBox="0 0 99 103"><rect x="17" y="18" width="65" height="67" rx="13" fill="none" stroke="#fff" stroke-width="6"/><line x1="49" y1="30" x2="49" y2="55" stroke="#fff" stroke-width="4"/><line x1="49" y1="55" x2="70" y2="55" stroke="#fff" stroke-width="4"/><circle cx="49" cy="55" r="4" fill="#fff"/></svg>
    </div>
    <!-- row 4 -->
    <div class="key tilt-forward" style="left:21px;top:367px;background:var(--teal)">
      <svg viewBox="0 0 99 103"><rect x="38" y="26" width="42" height="42" rx="8" transform="rotate(-25 59 47)" fill="none" stroke="#fff" stroke-width="6"/><path d="M13 80 A30 30 0 0 1 52 52" fill="none" stroke="#fff" stroke-width="6"/><path d="M50 40 L66 56 L47 62 Z" fill="#fff"/></svg>
    </div>
    <div class="key tilt-back" style="left:130px;top:367px;background:var(--teal)">
      <svg viewBox="0 0 99 103"><rect x="38" y="28" width="44" height="44" rx="8" transform="rotate(25 60 50)" fill="none" stroke="#fff" stroke-width="6"/><path d="M60 75 A24 24 0 0 0 20 62" fill="none" stroke="#fff" stroke-width="6"/><path d="M10 66 L30 52 L30 72 Z" fill="#fff"/></svg>
    </div>
    <div class="key mixer" style="left:242px;top:367px;background:var(--green)">
      <svg viewBox="0 0 99 103"><rect x="17" y="18" width="65" height="67" rx="13" fill="none" stroke="#fff" stroke-width="6"/><text class="key-label" x="49.5" y="47" font-size="11" text-anchor="middle" letter-spacing="0.5">MIXER</text><text class="key-label" x="49.5" y="65" font-size="11" text-anchor="middle">ON/OFF</text></svg>
    </div>
    <div class="key mix-direction" style="left:350px;top:367px;background:var(--pale)">
      <svg viewBox="0 0 99 103"><path d="M16 48 A33 33 0 0 1 68 24" fill="none" stroke="#fff" stroke-width="7"/><path d="M62 10 L84 22 L64 36 Z" fill="#fff"/><path d="M22 66 A33 33 0 0 0 68 80" fill="none" stroke="#fff" stroke-width="7"/><path d="M62 66 L86 72 L70 92 Z" fill="#fff"/></svg>
    </div>
    <!-- row 5 -->
    <div class="key heating" style="left:21px;top:504px;background:var(--red-deep)">
      <svg viewBox="0 0 99 103"><rect x="17" y="18" width="65" height="67" rx="13" fill="none" stroke="#fff" stroke-width="6"/><g fill="none" stroke="#fff" stroke-width="4"><path d="M37 74 c-8 -10 8 -16 0 -26 c-6 -8 2 -12 2 -16"/><path d="M50 74 c-8 -10 8 -16 0 -26 c-6 -8 2 -12 2 -16"/><path d="M63 74 c-8 -10 8 -16 0 -26 c-6 -8 2 -12 2 -16"/></g><line x1="27" y1="75" x2="72" y2="75" stroke="#fff" stroke-width="4"/></svg>
    </div>
    <div class="key reset" style="left:130px;top:504px;background:var(--lavender)">
      <svg viewBox="0 0 99 103"><path d="M32 26 H78 a6 6 0 0 1 6 6 V86 a6 6 0 0 1 -6 6 H22 V76" fill="none" stroke="#fff" stroke-width="6"/><path d="M6 26 L34 10 V42 Z" fill="#fff"/><text class="key-label" x="51" y="74" font-size="11" text-anchor="middle" letter-spacing="1">RESET</text></svg>
    </div>
    <!-- knob -->
    <svg class="knob" viewBox="0 0 110 110">
      <g fill="none" stroke="var(--knob-ring)" stroke-linecap="butt">
        <path d="M22 30 A42 42 0 0 1 48 13" stroke-width="6"/>
        <path d="M55 11 A44 44 0 0 1 82 20" stroke-width="8"/>
        <path d="M87 25 A46 46 0 0 1 100 50" stroke-width="10"/>
        <path d="M101 58 A48 48 0 0 1 88 92" stroke-width="12"/>
        <path d="M15 45 A42 42 0 0 0 16 70" stroke-width="3"/>
        <path d="M18 76 A42 42 0 0 0 24 87" stroke-width="2"/>
      </g>
      <circle cx="55" cy="55" r="37" fill="var(--knob)"/>
    </svg>
  </div>
  <!-- emergency stop -->
  <svg class="estop" viewBox="0 0 280 280">
    <defs>
      <path id="estop-track" d="M28 140 a112 112 0 1 1 224 0 a112 112 0 1 1 -224 0"/>
    </defs>
    <circle cx="140" cy="140" r="140" fill="var(--estop-ring)"/>
    <circle cx="140" cy="140" r="90" fill="var(--estop-button)"/>
    <text font-family="'Open Sans', Arial, sans-serif" font-weight="700" font-size="17" fill="var(--ink)" letter-spacing="3">
      <textPath href="#estop-track" startOffset="25%" text-anchor="middle">EMERGENCY STOP</textPath>
    </text>
    <text font-family="'Open Sans', Arial, sans-serif" font-weight="700" font-size="17" fill="var(--ink)" letter-spacing="3">
      <textPath href="#estop-track" startOffset="75%" text-anchor="middle">EMERGENCY STOP</textPath>
    </text>
  </svg>
</div>
</body>
</html>
```